R&T Clearcoat Stripping Business Card

We are in need of a business card design for our new Texas based company called 'R&T Clearcoat Stripping'. Our new innovative mobile media blasting service utilizes recycled material and a new water based process that eliminates all dust (i.e. as apposed to the old sand blasting format). Our 'advanced surface preparation' service targets multiple industries such as automotive, Industrial, marine and structural (graffiti removal). We would like to see the design include a recycling type logo or concept that utilizes colors such as black, various shades of green, some white, yellow and/or grey (e.g. perhaps a blackish background). The final design should look simple and professional and should clearly communicate the environmentally friendly approach through logo or design (i.e. Eco-Friendly, Go Green or Blast Green methodologies). Thank you in advance!
Updates

Please pardon any inconvenience. We have decided to pursue a two sided business card. All original information/designs requirements remains the same for the front. However, we would like back of the card to state the following: "We bring the power of Dustless Media Blasting equipment to your location. We can remove any coating from any surface. Bullets include: Paint Stripping, Auto Restoration, Graffiti Removal, Black Walls & Stone, Concrete, Boats, Iron Fences, Tractors & Trailers, Pools & Fountains, Wood Restoration.

Industry/Entity Type

Recycling

Contact Information for Business Card

R&T Clearcoat Stripping, LLC - Derek Kovel, MBA, PMP - cell: 915-382-6091, office: 915-207-5839 - dkovel@rtclearcoatstripping.com - CEO/Founder

Requirements
Must have
• Recycle or environmentally friendly logos or design.
Nice to have
• Business oriented design with an aggressive look. Also, if possible would like to see R&T incorporated into the design or logo. Please note that we have decided to add the option of adding details to the back of the card (2 sided). The front should contain the logo/design and the back should have the following details listed: "We bring the power of Dustless Media Blasting equipment to your location. We can remove any coating from any surface. Bullets include: Paint Stripping, Auto Restoration, Graffiti Removal, Black Walls & Stone, Concrete, Boats, Iron Fences, Tractors & Trailers, Pools & Fountains, Wood Restoration.

```html
<!DOCTYPE html>
<html lang="en">
<head>
<meta charset="utf-8">
<title>R&amp;T Clearcoat Stripping — Business Card</title>
<link href="https://fonts.googleapis.com/css2?family=Lato:wght@400;700&display=swap" rel="stylesheet">
<style>
  :root {
    --stage: #d9d9d9;
    --card-dark: #2b2b2b;
    --card-light: #ffffff;
    --ink: #2a2a2a;
    --green: #3fa548;
    --white: #ffffff;
  }
  * { box-sizing: border-box; margin: 0; padding: 0; }
  html, body { width: 1200px; height: 900px; overflow: hidden; }
  body {
    background: var(--stage);
    font-family: "Lato", Arial, sans-serif;
    position: relative;
  }
  .card {
    position: absolute;
    width: 630px;
    height: 360px;
    box-shadow: 0 8px 24px rgba(0,0,0,0.25);
    overflow: hidden;
  }
  .card-front { left: 60px; top: 70px; background: var(--card-dark); }
  .card-back { left: 510px; top: 470px; background: var(--card-light); }

  .wordmark {
    display: flex;
    align-items: center;
    gap: 16px;
    font-weight: 700;
    line-height: 1.15;
  }
  .wordmark-dot {
    flex: none;
    width: 46px;
    height: 46px;
    border-radius: 50%;
    background: var(--green);
  }
  .card-front .wordmark {
    position: absolute;
    left: 50%; top: 50%;
    transform: translate(-50%, -50%);
    color: var(--white);
    font-size: 34px;
    width: 420px;
  }
  .card-back .wordmark {
    position: absolute;
    left: 40px; top: 160px;
    color: var(--ink);
    font-size: 26px;
    width: 290px;
  }
  .card-back .wordmark-dot { width: 38px; height: 38px; }

  .contact {
    position: absolute;
    left: 350px; top: 60px;
    color: var(--ink);
  }
  .contact-name { color: var(--green); font-size: 22px; font-weight: 400; }
  .contact-credentials { font-size: 14px; }
  .contact-title { font-size: 15px; margin: 2px 0 0 14px; }
  .contact-list { list-style: none; margin: 26px 0 0 40px; font-size: 15px; }
  .contact-list li { display: flex; align-items: center; gap: 10px; margin-bottom: 6px; }
  .contact-list svg { width: 14px; height: 14px; fill: var(--green); flex: none; }

  .card-edge {
    position: absolute;
    left: 0; right: 0; bottom: 0;
    height: 16px;
    display: flex;
  }
  .card-edge-dark { flex: 7; background: var(--card-dark); }
  .card-edge-green { flex: 3; background: var(--green); }
</style>
</head>
<body>
  <section class="card card-front" aria-label="Card front">
    <div class="wordmark">
      <span class="wordmark-dot"></span>
      <span>R&amp;T Clearcoat Stripping, LLC</span>
    </div>
  </section>

  <section class="card card-back" aria-label="Card back">
    <div class="wordmark">
      <span class="wordmark-dot"></span>
      <span>R&amp;T Clearcoat Stripping, LLC</span>
    </div>

    <div class="contact">
      <p class="contact-name">Derek Kovel, <span class="contact-credentials">MBA, PMP</span></p>
      <p class="contact-title">CEO/Founder</p>
      <ul class="contact-list">
        <li>
          <svg viewBox="0 0 16 16" aria-hidden="true"><path d="M3.5 1l2.5 3-1.5 2c1 2 3 4 5 5l2-1.5 3 2.5-1.5 2.5C8 15 1 8 1 2.5z"/></svg>
          915-207-5839
        </li>
        <li>
          <svg viewBox="0 0 16 16" aria-hidden="true"><path d="M4 0h8a1 1 0 0 1 1 1v14a1 1 0 0 1-1 1H4a1 1 0 0 1-1-1V1a1 1 0 0 1 1-1zm1 2v10h6V2zm3 11a1 1 0 1 0 0 2 1 1 0 0 0 0-2z"/></svg>
          915-382-6091
        </li>
        <li>
          <svg viewBox="0 0 16 16" aria-hidden="true"><path d="M0 3h16v1.5L8 9 0 4.5zM0 6l8 4.5L16 6v7H0z"/></svg>
          dkovel@rtclearcoatstripping.com
        </li>
      </ul>
    </div>

    <div class="card-edge">
      <span class="card-edge-dark"></span>
      <span class="card-edge-green"></span>
    </div>
  </section>
</body>
</html>
```